Hello my name is Colin, I am Starting a business called Harbor Health and fitness and am in need of a memorable business card.
It is a personal training studio. I have added the logo that i would like to be on the left center om my business card. i would like room left up the top for a heading sentence such as. "Is your body shocking for all the wrong reasons". there must be room left on the right of the logo below the main heading for 3 sub headings.
then under those 3 headings and logo room for another larger heading eg. "give me a call and learn how to eat chocolate, drink bear and have great sex". in what room is left i would like to be used for my contact details, use I'm Colin Fairweather your fitness expert on the left then on the right Phone, Email and website space in at least 12 Point. Very specific i know :) now onto the back, for the back i would like an eye catching graphic and room for one main headline and 3 bullet points centered just write anything i will choose what to put in them when i pick a winner. Thank you very much for sticking through all of that :) i appreciate you taking the time to read it and hopefully undergo designing me a business card.
I can't wait to see the designs!

Target Market(s)

slightly more towards females although it would probably be best if it was targeted towards both sexes

Industry/Entity Type

Training

Requirements
Nice to have
• I would love to see if anyone could come up with a design that would really make my card stand out and be memorable.
Should not have
• tacky fitness photos of abs and muscles etc.

```html
<!DOCTYPE html>
<html lang="en">
<head>
<meta charset="utf-8">
<title>Harbor Health and Fitness – Business Cards</title>
<link href="https://fonts.googleapis.com/css2?family=Questrial&family=Source+Sans+3:wght@400;600;700&family=Jost:wght@400;600&display=swap" rel="stylesheet">
<style>
  :root {
    --backdrop: #6e3a22;
    --paper: #ffffff;
    --navy: #1b4f86;
    --navy-deep: #0f3766;
    --navy-mid: #1a4b82;
    --ink: #1c1c1c;
    --grey: #555a60;
    --watermark-light: #e6e8ef;
    --watermark-dark: rgba(255,255,255,0.12);
    --blush-1: #ecdccf;
    --blush-2: #e2c7bb;
    --blush-3: #f1e4d8;
  }
  * { box-sizing: border-box; margin: 0; padding: 0; }
  html, body { width: 1200px; height: 745px; overflow: hidden; }
  body { background: var(--backdrop); font-family: "Questrial", sans-serif; }
  .sheet { position: relative; width: 1200px; height: 745px; }

  .card { position: absolute; width: 524px; height: 299px; overflow: hidden; }
  .card--front { left: 55px; top: 53px; background: var(--paper); }
  .card--pattern { left: 604px; top: 60px; }
  .card--light { left: 57px; top: 394px; background: var(--paper); }
  .card--navy { left: 615px; top: 400px; background: linear-gradient(180deg, var(--navy-mid), var(--navy-deep)); }

  /* Front */
  .brand { position: absolute; left: 26px; top: 20px; color: var(--navy); font-family: "Questrial", sans-serif; font-weight: 400; }
  .brand__name { display: block; font-size: 74px; line-height: 76px; letter-spacing: -1px; }
  .brand__tag { display: block; font-size: 21px; line-height: 22px; margin-left: 64px; }

  .owner { position: absolute; left: 26px; top: 136px; }
  .owner__name { font-family: "Source Sans 3", sans-serif; font-weight: 600; font-size: 21px; color: var(--navy); line-height: 24px; }
  .owner__role { font-size: 16px; color: var(--grey); line-height: 20px; }

  .contact { position: absolute; left: 26px; top: 193px; list-style: none; color: var(--grey); }
  .contact li { display: flex; align-items: center; gap: 6px; height: 34px; font-size: 20px; }
  .contact svg { width: 17px; height: 17px; flex: none; }

  .pitch { position: absolute; left: 302px; top: 13px; width: 215px; color: var(--grey); }
  .pitch__headline { font-family: "Source Sans 3", sans-serif; font-weight: 700; font-size: 14.5px; line-height: 18px; color: var(--navy); }
  .pitch__intro { font-size: 13.5px; line-height: 16px; margin-top: 20px; }
  .pitch__points { list-style: none; font-size: 13.5px; line-height: 20px; margin-top: 21px; }
  .pitch__points li::before { content: "• "; }
  .pitch__offer { font-size: 17px; line-height: 20px; margin-top: 20px; }
  .pitch__offer span { display: block; }
  .pitch__offer .gap { margin-top: 5px; }

  /* Backs */
  .artwork { position: absolute; inset: 0;
    background: radial-gradient(ellipse at 50% 55%, var(--blush-3), var(--blush-1) 55%, var(--blush-2)); }
  .back-copy { position: absolute; left: 0; right: 0; top: 83px; text-align: center; font-family: "Jost", sans-serif; font-size: 24px; line-height: 30px; }
  .back-copy__points { list-style: none; display: inline-block; text-align: left; margin-top: 3px; }
  .back-copy__points li::before { content: "• "; }
  .back-copy__url { position: absolute; left: 0; right: 0; bottom: 17px; text-align: center; font-family: "Jost", sans-serif; font-weight: 600; font-size: 21px; letter-spacing: 3.2px; }
  .card--pattern .back-copy, .card--pattern .back-copy__url { color: var(--ink); }
  .card--light .back-copy, .card--light .back-copy__url { color: #333; }
  .card--navy .back-copy, .card--navy .back-copy__url { color: #fff; }

  .watermark { position: absolute; left: 45px; top: 52px; font-family: "Questrial", sans-serif; }
  .watermark__name { display: block; font-size: 150px; line-height: 150px; letter-spacing: -2px; }
  .watermark__tag { display: block; font-size: 33px; line-height: 34px; margin-left: 150px; margin-top: -8px; }
  .card--light .watermark { color: var(--watermark-light); }
  .card--navy .watermark { color: var(--watermark-dark); }
</style>
</head>
<body>
<main class="sheet">

  <section class="card card--front" aria-label="Front of card">
    <div class="brand">
      <span class="brand__name">Harbor</span>
      <span class="brand__tag">Health and Fitness</span>
    </div>

    <div class="owner">
      <p class="owner__name">Colin Fairweather</p>
      <p class="owner__role">Fitness expert</p>
    </div>

    <ul class="contact">
      <li>
        <svg viewBox="0 0 20 20" aria-hidden="true"><circle cx="10" cy="10" r="8.5" fill="none" stroke="currentColor" stroke-width="1.6"/><path d="M7 5.5c-1 1-1 3 1 5.5s4.5 3.5 5.5 2.5l.5-1-2-1.5-1 .8c-1-.5-2-1.6-2.6-2.6l.8-1L8 5z" fill="currentColor"/></svg>
        0912 345678
      </li>
      <li>
        <svg viewBox="0 0 20 20" aria-hidden="true"><rect x="2" y="5" width="16" height="11" rx="1.5" fill="currentColor"/><path d="M2.5 6l7.5 5.5L17.5 6" fill="none" stroke="#fff" stroke-width="1.4"/></svg>
        info@harborfit.com
      </li>
      <li>
        <svg viewBox="0 0 20 20" aria-hidden="true"><g fill="none" stroke="currentColor" stroke-width="1.4"><circle cx="10" cy="10" r="8"/><ellipse cx="10" cy="10" rx="3.5" ry="8"/><path d="M2 10h16M3.5 6h13M3.5 14h13"/></g></svg>
        www.harborfit.com
      </li>
    </ul>

    <div class="pitch">
      <h1 class="pitch__headline">Is your body shocking for<br>all the wrong reasons</h1>
      <p class="pitch__intro">Lorem ipsum Lorem ipsum<br>Lorem ipsum</p>
      <ul class="pitch__points">
        <li>Lorem ipsum diet</li>
        <li>Lorem ipsum diet</li>
        <li>Lorem ipsum diet</li>
      </ul>
      <p class="pitch__offer">
        <span>Give me a call and</span>
        <span>Learn how to eat chocolate</span>
        <span>drink bear</span>
        <span class="gap">Have great sex</span>
      </p>
    </div>
  </section>

  <section class="card card--pattern" aria-label="Back of card, ornamental version">
    <div class="artwork" role="img" aria-label="Soft blush paisley and floral ornamental pattern"></div>
    <div class="back-copy">
      <p>Lorem Ispum Lorem Ispum Lorem Ispum</p>
      <ul class="back-copy__points">
        <li>Lorem Ispum Lorem</li>
        <li>Lorem Ispum Lorem</li>
        <li>Lorem Ispum Lorem</li>
      </ul>
    </div>
    <p class="back-copy__url">www.harborhealthfit.com</p>
  </section>

  <section class="card card--light" aria-label="Back of card, white version">
    <div class="watermark" aria-hidden="true">
      <span class="watermark__name">Harbor</span>
      <span class="watermark__tag">Health and Fitness</span>
    </div>
    <div class="back-copy">
      <p>Lorem Ispum Lorem Ispum Lorem Ispum</p>
      <ul class="back-copy__points">
        <li>Lorem Ispum Lorem</li>
        <li>Lorem Ispum Lorem</li>
        <li>Lorem Ispum Lorem</li>
      </ul>
    </div>
    <p class="back-copy__url">www.harborhealthfit.com</p>
  </section>

  <section class="card card--navy" aria-label="Back of card, navy version">
    <div class="watermark" aria-hidden="true">
      <span class="watermark__name">Harbor</span>
      <span class="watermark__tag">Health and Fitness</span>
    </div>
    <div class="back-copy">
      <p>Lorem Ispum Lorem Ispum Lorem Ispum</p>
      <ul class="back-copy__points">
        <li>Lorem Ispum Lorem</li>
        <li>Lorem Ispum Lorem</li>
        <li>Lorem Ispum Lorem</li>
      </ul>
    </div>
    <p class="back-copy__url">www.harborhealthfit.com</p>
  </section>

</main>
</body>
</html>
```